Business Card Design Project

I need a cool business card design for the company that will build residential houses.
The card should include:
1) Name: Borek Valdisov
2) Cell: 587.244.XXXX
3) Email: bor.valdisov@qorvina.example
4) Position: General Manager
5) Residential Home Building
6) Company logo that I have uploaded

Industry/Entity Type

Residential

```html
<!DOCTYPE html>
<html lang="en">
<head>
<meta charset="utf-8">
<title>Qorvina Developments – Business Card</title>
<link rel="stylesheet" href="https://fonts.googleapis.com/css2?family=Share+Tech+Mono&family=Open+Sans:wght@600&display=swap">
<style>
  :root {
    --backdrop: #232323;
    --card: #ffffff;
    --green: #6cb64b;
    --band: #72b84f;
    --brand-blue: #1d5cae;
    --white: #ffffff;
  }
  html, body {
    margin: 0;
    padding: 0;
    width: 1200px;
    height: 1200px;
    overflow: hidden;
    background: var(--backdrop);
  }
  .canvas {
    position: relative;
    width: 1200px;
    height: 1200px;
  }
  .card {
    position: absolute;
    left: 235px;
    top: 377px;
    width: 714px;
    height: 445px;
    background: var(--card);
  }
  .brand {
    position: absolute;
    left: 38px;
    top: 107px;
    width: 336px;
    height: 194px;
    display: flex;
    align-items: center;
    justify-content: center;
    gap: 12px;
  }
  .brand-mark {
    width: 26px;
    height: 26px;
    border-radius: 50%;
    background: var(--brand-blue);
    flex: none;
  }
  .brand-name {
    font-family: "Share Tech Mono", monospace;
    font-size: 27px;
    color: var(--brand-blue);
    line-height: 1.1;
    white-space: nowrap;
  }
  .divider {
    position: absolute;
    left: 391px;
    top: 131px;
    width: 3px;
    height: 153px;
    background: var(--green);
  }
  .contact {
    position: absolute;
    left: 420px;
    top: 136px;
    width: 252px;
    color: var(--green);
  }
  .person-name {
    font-family: "Share Tech Mono", monospace;
    font-size: 27px;
    line-height: 30px;
    margin: 0 0 0 2px;
    letter-spacing: 0.5px;
  }
  .person-role {
    font-family: "Share Tech Mono", monospace;
    font-size: 18px;
    line-height: 20px;
    margin: 1px 0 0 30px;
  }
  .rule {
    height: 2px;
    background: var(--green);
    margin: 6px 0 0;
  }
  .contact-row {
    display: flex;
    align-items: center;
    gap: 6px;
    font-family: "Open Sans", sans-serif;
    font-weight: 600;
    height: 52px;
    margin-top: 0;
  }
  .contact-row.phone { font-size: 19px; height: 51px; }
  .contact-row.email { font-size: 16.5px; height: 48px; }
  .contact-row svg { flex: none; }
  .tagline-band {
    position: absolute;
    left: 0;
    top: 384px;
    width: 714px;
    height: 39px;
    background: var(--band);
    display: flex;
    align-items: center;
    justify-content: center;
    font-family: "Share Tech Mono", monospace;
    font-size: 24px;
    color: var(--white);
    letter-spacing: 0.5px;
  }
</style>
</head>
<body>
<div class="canvas">
  <div class="card">
    <div class="brand">
      <span class="brand-mark"></span>
      <span class="brand-name">Qorvina Developments</span>
    </div>

    <div class="divider"></div>

    <div class="contact">
      <p class="person-name">Borek Valdisov</p>
      <p class="person-role">General Manager</p>
      <div class="rule"></div>
      <div class="contact-row phone">
        <svg width="14" height="22" viewBox="0 0 14 22" aria-hidden="true">
          <rect x="1.5" y="3" width="11" height="18" rx="2" fill="none" stroke="currentColor" stroke-width="2"/>
          <line x1="3.5" y1="0.5" x2="3.5" y2="3" stroke="currentColor" stroke-width="2"/>
          <rect x="4" y="6" width="6" height="5" fill="currentColor"/>
          <rect x="4" y="13" width="6" height="5" fill="currentColor" opacity="0.6"/>
        </svg>
        <span>587.244.XXXX</span>
      </div>
      <div class="rule"></div>
      <div class="contact-row email">
        <svg width="20" height="15" viewBox="0 0 20 15" aria-hidden="true">
          <rect x="1" y="1" width="18" height="13" fill="none" stroke="currentColor" stroke-width="1.5"/>
          <polyline points="1,1 10,8 19,1" fill="none" stroke="currentColor" stroke-width="1.5"/>
        </svg>
        <span>bor.valdisov@qorvina.example</span>
      </div>
    </div>

    <div class="tagline-band">Residential Home Building</div>
  </div>
</div>
</body>
</html>
```